Business Card design for Property Developer

We need a business card design for a Melbourne based Property Developer called "Kestrel Grove Pty Ltd".

We subdivide land and onsell to builders etc.

We already have a company logo, which is attached. Also I have attached the layout requirements from the printer. We would like a 2-sided design with one side displaying our logo by itself and the other with the required info, such as name, address, tel no., email, abn etc. The card will need to be used by 4 members of staff so name and contact details should be interchangable.
Updates

If possible, can you please write "name' "job position" "phone" "email" "address" on the card but leave them so I can add the details at a later time. Thank you. Also I plan on printing with UV spot printing as a background on the card. Keep this is mind when designing.

Thanks again.

Hello designers, please do not include pics of houses, house plansĀ or construction machinery etc as we really do not like the way it looks. Thank you.

Target Market(s)

Real Estate Agents, Land Owners, Local Council Departments, Govt Bodies, other Developers etc.

Industry/Entity Type

Business

Requirements
Must have
• 2-sided design with one side displaying our logo by itself and the other with the required info, such as name, address, tel no., email, abn etc.

```html
<!DOCTYPE html>
<html lang="en">
<head>
<meta charset="utf-8">
<title>Kestrel Grove – Business Card</title>
<link href="https://fonts.googleapis.com/css2?family=Source+Sans+3:wght@400;600;700&display=swap" rel="stylesheet">
<style>
  :root {
    --backdrop: #ece8e4;
    --card-white: #ffffff;
    --card-shade: #f4f4f4;
    --brand-red: #e31e26;
    --brand-red-deep: #9c1219;
    --brand-red-mid: #c8161e;
    --brand-blue: #2b62b8;
    --ink: #1f1f1f;
    --ink-soft: #2e2e2e;
  }
  * { box-sizing: border-box; margin: 0; padding: 0; }
  html, body {
    width: 1200px; height: 900px; overflow: hidden;
    background: var(--backdrop);
    font-family: "Source Sans 3", "Myriad Pro", Arial, sans-serif;
  }
  .stage {
    position: relative; width: 1200px; height: 900px;
    display: flex; justify-content: center; align-items: center; gap: 46px;
  }
  .card {
    position: relative; width: 320px; height: 508px; overflow: hidden;
    box-shadow: 0 2px 6px rgba(0,0,0,.18);
  }

  /* Information side */
  .card--info {
    background: linear-gradient(180deg, var(--card-white) 0%, var(--card-shade) 100%);
  }
  .brand {
    position: absolute; left: 0; right: 0; text-align: center;
  }
  .brand__mark {
    display: block; margin: 0 auto; border-radius: 50%;
  }
  .brand__name {
    display: block; font-weight: 700; text-transform: uppercase;
    letter-spacing: 1px; line-height: 1;
  }
  .card--info .brand { top: 26px; }
  .card--info .brand__mark { width: 86px; height: 86px; background: var(--brand-blue); }
  .card--info .brand__name { margin-top: 26px; font-size: 29px; color: var(--brand-red); }

  .person { position: absolute; left: 20px; top: 318px; }
  .person__name { font-size: 21px; font-weight: 700; color: var(--brand-red); line-height: 1.1; }
  .person__role { font-size: 14.5px; color: var(--ink-soft); line-height: 1.2; }
  .person__rule {
    position: absolute; left: 0; top: 365px; width: 196px; height: 2px;
    background: var(--brand-red);
  }
  .company { position: absolute; left: 20px; top: 375px; font-size: 14.5px; color: var(--ink-soft); line-height: 19px; }
  .company__name { font-weight: 700; color: var(--ink); }
  .contact { position: absolute; left: 20px; top: 447px; font-size: 14.5px; color: var(--ink-soft); line-height: 19px; }
  .contact__line { display: flex; align-items: center; gap: 3px; }
  .contact__icon { width: 16px; height: 12px; flex: none; }

  /* Logo side */
  .card--logo {
    background: radial-gradient(ellipse 78% 48% at 50% 60%, var(--brand-red) 0%, var(--brand-red-mid) 55%, var(--brand-red-deep) 100%);
  }
  .card--logo .brand { top: 164px; }
  .card--logo .brand__mark { width: 104px; height: 104px; background: var(--brand-blue); }
  .card--logo .brand__name { margin-top: 30px; font-size: 33px; color: var(--card-white); }
  .website {
    position: absolute; left: 0; right: 0; bottom: 18px; text-align: center;
    font-size: 12px; letter-spacing: 2.4px; color: var(--card-white);
  }
</style>
</head>
<body>
<main class="stage">

  <section class="card card--info" aria-label="Business card, contact side">
    <div class="brand">
      <span class="brand__mark"></span>
      <span class="brand__name">Kestrel Grove</span>
    </div>

    <div class="person">
      <p class="person__name">Daniel Rowe</p>
      <p class="person__role">Company Director</p>
    </div>
    <div class="person__rule"></div>

    <div class="company">
      <p class="company__name">Kestrel Grove Pty Ltd</p>
      <p>17 harbour view lane, Greyfield</p>
      <p>County Mead BT31 4QX</p>
    </div>

    <div class="contact">
      <p class="contact__line">
        <svg class="contact__icon" viewBox="0 0 16 12" aria-hidden="true">
          <path d="M2 4 C4 1 12 1 14 4 L12 5.5 L10.5 3.5 H5.5 L4 5.5 Z" fill="var(--brand-red)"/>
          <rect x="4" y="6" width="8" height="5" rx="1" fill="var(--brand-red)"/>
        </svg>
        <span>: 0791-405-2273</span>
      </p>
      <p class="contact__line">
        <svg class="contact__icon" viewBox="0 0 16 12" aria-hidden="true">
          <rect x="1.5" y="1.5" width="13" height="9" fill="none" stroke="var(--brand-red)" stroke-width="1.4"/>
          <path d="M1.5 1.5 L8 7 L14.5 1.5 M1.5 10.5 L6 6 M14.5 10.5 L10 6" fill="none" stroke="var(--brand-red)" stroke-width="1.2"/>
        </svg>
        <span>: daniel@kestrelgrove.com</span>
      </p>
    </div>
  </section>

  <section class="card card--logo" aria-label="Business card, brand side">
    <div class="brand">
      <span class="brand__mark"></span>
      <span class="brand__name">Kestrel Grove</span>
    </div>
    <p class="website">www.kestrelgrove.com</p>
  </section>

</main>
</body>
</html>
```